Sports Membership Website with an App

My client is a Professional Sports Handicapper (Sports Bettor) and we are creating a new website with an App for their service.

The website will be a paid membership website where the user can subscribe to a premium membership sports betting pick and advice. Premium members will also be able to view statistics on their picks and their overall progress.

For the website we will be building a custom theme from scratch and will use Bootstrap to control the framework. To show statistics we will be using Chart.js. The line graph and Donut graph will be the most used graph types.

The sports that my client covers are QRT, WLK, ZPD, GVOTE, GVOTY and GVOTEM. You will need to incorporate their respective logos into the design somehow.

The landing page will show statistics for ZPD, WLK, GVOTY and GVOTEM. Please use dummy data to represent this. Data will be Overall Picks (100), Wins (75), Losses (25)

We will also offer affiliate links for users to click and sign up like they have on the websites www.tallyorbit.com.au. Affiliate links must be consistent in look but have their own respective logos. The sites that we will focus on will be Mossbeck and 9 quills.

You will need to create a landing page, members area and subscriptions page.

Websites we like
www.tallyorbit.com.au - layout and feel
http://glimmer-demo.vostrakel.me/glimmer-portal-hub-site-theme/index.html - great members area

Services Similar to ours
www.sages.brindlepost.com
www.marlowgameforecasting.com

Colour scheme is black, red, grey, light grey

Industry/Entity Type

Gambling

Number of Pages Required

3 page

Font styles to use
Sans Serif

Colors
f04a50

Requirements
Must have
• Must be modern and professional.
• I like the components from https://layoutbazaar.example/item/corvina-ui-pack-wide-set-of-ui-parts/58210374?s_rank=1 as they are modern and sleek
Nice to have
• Think outside the box. This website is to provide a service where the user receives a new pick to wager money on and then the system will keep track of their historical record to let the user know what their profit/loss is
Should not have
• Must be professional!

```html
<!DOCTYPE html>
<html lang="en">
<head>
<meta charset="utf-8">
<title>Flint Ram – Sports Handicapping Service</title>
<link href="https://fonts.googleapis.com/css2?family=Montserrat:ital,wght@0,500;0,600;0,700;1,600&family=Roboto:wght@400;500&display=swap" rel="stylesheet">
<style>
:root{
  --red:#e3262b;
  --red-deep:#d42426;
  --black:#1f1f1f;
  --charcoal:#3a3434;
  --grey:#5f6368;
  --grey-text:#8a8a8a;
  --light:#f2f2f2;
  --light-2:#e6e6e6;
  --white:#ffffff;
}
*{margin:0;padding:0;box-sizing:border-box}
html,body{width:1200px;height:2394px;overflow:hidden;background:var(--white)}
body{font-family:'Roboto',Arial,sans-serif;color:var(--black);position:relative}
.abs{position:absolute}
.head-font{font-family:'Montserrat',Arial,sans-serif}

/* Header */
.site-header{position:absolute;left:0;top:0;width:1200px;height:120px;background:var(--white);box-shadow:0 2px 6px rgba(0,0,0,.06);z-index:2}
.topbar{position:absolute;left:614px;top:0;width:586px;height:32px;background:var(--black);clip-path:polygon(0 0,100% 0,100% 100%,32px 100%)}
.social{position:absolute;top:0;height:32px;line-height:32px;font-size:11px;color:#ddd}
.btn-login{position:absolute;left:846px;top:0;width:76px;height:32px;background:#444;color:#fff;font-size:12px;line-height:32px;text-align:center;font-weight:500}
.btn-register{position:absolute;left:922px;top:0;width:123px;height:32px;background:var(--red);color:#fff;font-size:12px;line-height:32px;text-align:center;font-weight:500}
.search-icon{position:absolute;left:1062px;top:8px}
.brand{position:absolute;left:128px;top:30px;width:260px}
.brand-name{font-family:'Montserrat',Arial,sans-serif;font-weight:700;font-size:34px;color:var(--red);letter-spacing:1px;line-height:40px}
.brand-tag{font-family:'Montserrat',Arial,sans-serif;font-weight:600;font-size:10px;letter-spacing:2.6px;color:var(--black);margin-top:2px}
.main-nav{position:absolute;top:68px;left:0;font-size:15px;font-weight:500;color:var(--black)}
.main-nav span{position:absolute;white-space:nowrap}

/* Hero */
.hero{position:absolute;left:0;top:120px;width:1200px;height:507px;background:linear-gradient(180deg,#f4f4f4,#ffffff 60%,#f6f6f6)}
.hero-title{position:absolute;left:118px;top:122px;font-family:'Montserrat',Arial,sans-serif;font-size:41px;line-height:43px;font-weight:700}
.hero-title .lead{font-style:italic;font-weight:600;color:var(--black);display:block}
.hero-title .accent{color:var(--red);display:block}
.btn-join{position:absolute;left:118px;top:274px;width:236px;height:46px;background:var(--red);color:#fff;font-family:'Montserrat',Arial,sans-serif;font-weight:500;font-size:16px;line-height:46px;text-align:center}
.dots{position:absolute;left:115px;top:343px;display:flex;gap:8px}
.dots i{display:block;width:32px;height:3px;background:#bdbdbd}
.dots i.on{background:var(--black)}
.hero-photo{position:absolute;left:407px;top:32px;width:734px;height:475px;background:radial-gradient(ellipse at 55% 50%,#c9a9a2 0%,#d9cbc8 40%,#f1eeee 75%,rgba(255,255,255,0) 100%)}

/* Steps */
.steps{position:absolute;left:0;top:627px;width:1200px;height:390px;background:linear-gradient(180deg,#3a3333 0%,#7a2a2b 45%,var(--red-deep) 100%);color:#fff}
.notch{position:absolute;left:578px;top:0;width:0;height:0;border-left:22px solid transparent;border-right:22px solid transparent;border-top:22px solid #ffffff}
.section-title{position:absolute;left:0;width:100%;text-align:center;font-family:'Montserrat',Arial,sans-serif;font-weight:600;font-size:24px;letter-spacing:.5px}
.section-title .rule{display:inline-block;vertical-align:middle;width:56px;height:2px;background:currentColor;position:relative;margin:0 10px}
.section-title .rule::after{content:"";position:absolute;top:-3px;width:8px;height:8px;border-radius:50%;background:currentColor}
.section-title .rule.l::after{right:-2px}
.section-title .rule.r::after{left:-2px}
.step{position:absolute;top:110px;width:300px;text-align:center}
.step-icon{display:block;margin:0 auto;height:90px}
.step h3{font-family:'Montserrat',Arial,sans-serif;font-weight:600;font-size:19px;margin-top:46px;letter-spacing:.3px}
.step p{font-size:14px;line-height:21px;color:rgba(255,255,255,.55);margin-top:12px}
.step-arrow{position:absolute;top:160px}

/* About */
.about{position:absolute;left:0;top:1017px;width:1200px;height:408px;background:var(--white)}
.about h2{position:absolute;left:136px;top:75px;font-family:'Montserrat',Arial,sans-serif;font-weight:700;font-size:29px;color:var(--charcoal)}
.about h2 em{font-style:normal;color:var(--red)}
.about-copy{position:absolute;left:136px;top:126px;width:490px;font-size:14.5px;line-height:24px;color:var(--grey)}
.about-copy p+p{margin-top:10px}
.btn-more{position:absolute;left:136px;top:293px;width:156px;height:37px;background:linear-gradient(180deg,#4a4a4a,#222);color:#fff;font-family:'Montserrat',Arial,sans-serif;font-size:13px;font-weight:500;text-align:center;line-height:37px}
.about-photo{position:absolute;left:638px;top:0;width:463px;height:408px;background:radial-gradient(ellipse at 50% 55%,#d64040 0%,#e58c84 35%,#f6e4e1 65%,#ffffff 90%)}

/* Statistics */
.stats{position:absolute;left:0;top:1425px;width:1200px;height:359px;background:linear-gradient(180deg,#e4e2e2,#ecebeb 50%,#e2e0e0)}
.stats .section-title{top:44px;color:var(--charcoal)}
.tabs{position:absolute;left:278px;top:112px;display:flex}
.tab{width:157px;height:38px;line-height:38px;text-align:center;font-family:'Montserrat',Arial,sans-serif;font-weight:500;font-size:16px;background:#fff;color:var(--charcoal);border:1px solid #d0d0d0;position:relative}
.tab.active{background:var(--red);color:#fff;border-color:var(--red)}
.tab.active::after{content:"";position:absolute;left:68px;bottom:-10px;border-left:10px solid transparent;border-right:10px solid transparent;border-top:10px solid var(--red)}
.stat{position:absolute;top:180px;width:240px;text-align:center;font-family:'Montserrat',Arial,sans-serif;color:var(--grey)}
.stat .num{font-size:57px;font-weight:700;line-height:60px}
.stat .label{font-size:22px;font-weight:700;line-height:24px;margin-top:8px;color:#4f5358}

/* Premium */
.premium{position:absolute;left:0;top:1784px;width:1200px;height:316px;background:linear-gradient(180deg,#1d2024 0%,#2a2d30 45%,#244a22 75%,#1c3a1a 100%);color:#fff;text-align:center}
.premium h2{position:absolute;left:0;width:100%;top:70px;font-family:'Montserrat',Arial,sans-serif;font-weight:600;font-size:26px;letter-spacing:.4px}
.premium p{position:absolute;left:230px;width:740px;top:118px;font-size:17px;line-height:26px}
.btn-start{position:absolute;left:469px;top:192px;width:236px;height:46px;background:var(--red);color:#fff;font-family:'Montserrat',Arial,sans-serif;font-weight:500;font-size:16px;line-height:46px}

/* Leagues */
.leagues{position:absolute;left:0;top:2100px;width:1200px;height:157px;display:flex}
.league{width:300px;height:157px;display:flex;align-items:center;justify-content:center;gap:10px;background:var(--light);font-family:'Montserrat',Arial,sans-serif;font-weight:700;font-size:26px;color:var(--charcoal)}
.league.alt{background:var(--light-2)}
.league .mark{width:18px;height:18px;background:var(--red)}

/* Footer */
.site-footer{position:absolute;left:0;top:2257px;width:1200px;height:137px;background:var(--white);border-top:1px solid #ddd}
.footer-brand{position:absolute;left:128px;top:44px;font-family:'Montserrat',Arial,sans-serif;font-weight:700;font-size:30px;color:var(--red);letter-spacing:1px}
.footer-nav{position:absolute;right:128px;top:36px;font-size:15px;font-weight:500;display:flex;gap:21px}
.copyright{position:absolute;right:128px;top:68px;font-size:13px;color:#444}
</style>
</head>
<body>

<header class="site-header">
  <div class="topbar"></div>
  <span class="social" style="left:666px">Kite</span>
  <span class="social" style="left:702px">Folio</span>
  <span class="social" style="left:740px">Linkr</span>
  <span class="social" style="left:778px">Plaza</span>
  <div class="btn-login">LOGIN</div>
  <div class="btn-register">REGISTER FREE</div>
  <svg class="search-icon" width="16" height="16" viewBox="0 0 16 16"><circle cx="6.5" cy="6.5" r="4.8" fill="none" stroke="#fff" stroke-width="2"/><line x1="10" y1="10" x2="14.5" y2="14.5" stroke="#fff" stroke-width="2.2"/></svg>

  <div class="brand">
    <div class="brand-name">FLINTRAM</div>
    <div class="brand-tag">SPORTS HANDICAPPING SERVICE</div>
  </div>

  <nav class="main-nav">
    <span style="left:437px">FREE PICK</span>
    <span style="left:543px">LATEST TIPS</span>
    <span style="left:667px">JOIN</span>
    <span style="left:733px">SUBSCRIPTION</span>
    <span style="left:873px">SERVICES</span>
    <span style="left:975px">HELP</span>
    <span style="left:1045px">RESULT</span>
  </nav>
</header>

<section class="hero">
  <div class="hero-photo" role="img" aria-label="Group of athletes from basketball, football, boxing, hockey, tennis and baseball in action"></div>
  <h1 class="hero-title">
    <span class="lead">EXPERTS IN SPORTS</span>
    <span class="accent">BETTING PICK</span>
    <span class="accent">AND ADVICE</span>
  </h1>
  <div class="btn-join">JOIN FOR FREE &#8250;</div>
  <div class="dots"><i></i><i></i><i class="on"></i><i></i></div>
</section>

<section class="steps">
  <div class="notch"></div>
  <h2 class="section-title" style="top:46px"><span class="rule l"></span>HOW TO START BETTING<span class="rule r"></span></h2>

  <div class="step" style="left:123px">
    <svg class="step-icon" width="90" height="90" viewBox="0 0 90 90" fill="none" stroke="#fff" stroke-width="2.5">
      <circle cx="27" cy="20" r="8"/><circle cx="45" cy="14" r="9"/><circle cx="63" cy="20" r="8"/>
      <path d="M12 50 q0-16 15-18 M78 50 q0-16 -15-18 M28 48 q0-22 17-22 q17 0 17 22"/>
      <path d="M8 52 h74 l-8 10 8 10 h-20 l-6 10 h-22 l-6-10 h-20 l8-10z"/>
    </svg>
    <h3>1. JOIN US NOW</h3>
    <p>sociosqu ad litora torquent per conubia<br>nostra per inceptos hymenaeo</p>
  </div>
  <svg class="step-arrow" style="left:391px" width="78" height="20" viewBox="0 0 78 20"><line x1="0" y1="10" x2="76" y2="10" stroke="rgba(255,255,255,.35)" stroke-width="1.5"/><polyline points="66,1 76,10 66,19" fill="none" stroke="rgba(255,255,255,.35)" stroke-width="1.5"/></svg>

  <div class="step" style="left:455px">
    <svg class="step-icon" width="90" height="90" viewBox="0 0 90 90" fill="none" stroke="#fff" stroke-width="2.5">
      <path d="M36 14 q14 0 14 18 q0 12-8 18 q22 4 22 22 v6 h-52 v-6 q0-18 22-22 q-8-6-8-18 q0-18 14-18z"/>
      <path d="M54 10 q14 0 14 18 q0 12-8 18 q22 4 22 22 v6 h-12"/>
    </svg>
    <h3>2. CHOOSE A BOOKIE</h3>
    <p>sociosqu ad litora torquent per conubia<br>nostra per inceptos hymenaeo</p>
  </div>
  <svg class="step-arrow" style="left:731px" width="78" height="20" viewBox="0 0 78 20"><line x1="0" y1="10" x2="76" y2="10" stroke="rgba(255,255,255,.35)" stroke-width="1.5"/><polyline points="66,1 76,10 66,19" fill="none" stroke="rgba(255,255,255,.35)" stroke-width="1.5"/></svg>

  <div class="step" style="left:785px">
    <svg class="step-icon" width="90" height="90" viewBox="0 0 90 90">
      <ellipse cx="56" cy="30" rx="24" ry="16" fill="#fff"/><ellipse cx="56" cy="30" rx="9" ry="6" fill="#a52a2b"/>
      <ellipse cx="34" cy="56" rx="26" ry="18" fill="#fff"/><ellipse cx="34" cy="56" rx="10" ry="7" fill="#a52a2b"/>
      <ellipse cx="34" cy="56" rx="20" ry="13" fill="none" stroke="#a52a2b" stroke-width="3" stroke-dasharray="5 6"/>
    </svg>
    <h3>3. START BETTING</h3>
    <p>sociosqu ad litora torquent per conubia<br>nostra per inceptos hymenaeo</p>
  </div>
</section>

<section class="about">
  <h2>ABOUT <em>FLINT RAM</em></h2>
  <div class="about-copy">
    <p>Maecenas aliquet velit vel turpis Mauris neque metus malesuada nec ultricies sit amet porttitor mattis enim In massa</p>
    <p>est eget tempor cursus neque mi consectetuer mi a ultricies massa est sed nisl Class aptent taciti sociosqu ad litora torquent per conubia nostra per inceptos hymenaeos Proin nulla arcu</p>
  </div>
  <div class="btn-more">LEARN MORE</div>
  <div class="about-photo" role="img" aria-label="Excited fan in a red shirt holding a football and a fan of banknotes"></div>
</section>

<section class="stats">
  <h2 class="section-title"><span class="rule l"></span>RECENT STATISTICS<span class="rule r"></span></h2>
  <div class="tabs">
    <div class="tab active">ZPD</div>
    <div class="tab">WLK</div>
    <div class="tab">GVOTY</div>
    <div class="tab">GVOTEM</div>
  </div>
  <div class="stat" style="left:196px"><div class="num">100</div><div class="label">OVERALL<br>PICKS</div></div>
  <div class="stat" style="left:469px"><div class="num">75</div><div class="label">WINS</div></div>
  <div class="stat" style="left:743px"><div class="num">25</div><div class="label">LOSSES</div></div>
</section>

<section class="premium" role="img" aria-label="Floodlit football stadium at night">
  <h2>JOIN OUR PREMIUM MEMBERSHIP</h2>
  <p>Maecenas aliquet velit vel turpis Mauris neque metus malesuada nec ultricies sit amet porttitor mattis enim In massa est eget tempor cursus neque mi consectetuer m</p>
  <div class="btn-start">GET STARTED &#8250;</div>
</section>

<section class="leagues">
  <div class="league"><span class="mark"></span>WLK</div>
  <div class="league alt"><span class="mark"></span>QRT</div>
  <div class="league"><span class="mark"></span>GVOTE</div>
  <div class="league alt"><span class="mark"></span>ZPD</div>
</section>

<footer class="site-footer">
  <div class="footer-brand">FLINTRAM</div>
  <nav class="footer-nav">
    <span>HOME</span><span>FREE PICK</span><span>LATEST TIPS</span><span>JOIN</span><span>SUBSCRIPTION</span><span>SERVICES</span><span>HELP</span><span>RESULT</span>
  </nav>
  <div class="copyright">© 2018 Company Name&nbsp; All right reserved&nbsp; Terms of Use</div>
</footer>

</body>
</html>
```